A new company focused on starting and investing in transformative businesses.

We need a simple and clean website with a few pages. we like larkmeadow.com as a starting point. we want the landing page to be very simple with an option to click through on the top right into INVESTOR LOGIN. then we want to be able to scroll down to see more about our company.

Target Market(s)

professional

Coding

Coded - Design and coding required

Number of Pages Required

2 page

Font styles to use
Serif
Sans Serif

Requirements
Must have
• HALVERN BUILDERS logo (attached as a file) on the top with INVESTOR LOGIN as a click through on the right. Please model the click through from larkmeadow.com. The description (also written in attached file) should be on the landing page. we do not want to have to scroll to read the description.

Then we can scroll down to read more about Halvern including the mission and the two types of businesses. More is detailed on the attached file called "Halvern Website Syntax"
Should not have
• should not be slow loading with lots of fancy graphics. should not be busy and with too many colors.

```html
<!DOCTYPE html>
<html lang="en">
<head>
<meta charset="utf-8">
<title>Halvern Builders – Homepage Concepts</title>
<link rel="stylesheet" href="https://fonts.googleapis.com/css2?family=Lato:wght@400;700&family=Montserrat:wght@400;600&display=swap">
<style>
  :root{
    --board:#efefef;
    --white:#ffffff;
    --ink:#231f20;
    --muted:#6d6d6d;
    --icon:#555555;
    --blue:#0b5aa6;
    --footer:#231f20;
    --rule:#4a4647;
  }
  *{box-sizing:border-box;margin:0;padding:0}
  html,body{width:1062px;height:1200px;overflow:hidden;background:var(--board)}
  body{position:relative;font-family:"Lato",sans-serif;color:var(--ink)}

  .concept{position:absolute;width:440px;height:533px;background:var(--white);box-shadow:0 6px 22px rgba(0,0,0,.18);overflow:hidden}
  .concept--mountain{left:72px;top:50px}
  .concept--growth{left:550px;top:50px}
  .concept--meeting{left:330px;top:617px}

  .hero{position:relative;height:234px;color:var(--white)}
  .hero__media{position:absolute;inset:0}
  .concept--mountain .hero__media{background:linear-gradient(160deg,#d9dbd8 0%,#a9b3bb 35%,#7b8691 60%,#4d5258 80%,#2a2a2a 100%)}
  .concept--growth .hero__media{background:radial-gradient(circle at 85% 40%,#6d6d6d 0%,#3f3f3f 45%,#2a2a2a 100%)}
  .concept--meeting .hero__media{background:linear-gradient(120deg,#3a3a3a 0%,#6b6b6b 45%,#8a8a8a 60%,#4b4b4b 100%)}

  .brand{position:absolute;left:41px;top:11px;display:flex;align-items:center;gap:6px;font-family:"Montserrat",sans-serif;font-weight:600;font-size:11.5px;line-height:13px;letter-spacing:.3px;color:var(--white)}
  .brand__mark{width:22px;height:22px;background:currentColor}
  .hero--light .brand{color:var(--ink)}
  .hero--light .brand__mark{background:var(--blue)}

  .nav{position:absolute;right:41px;top:21px;display:flex;align-items:center;gap:19px;font-family:"Montserrat",sans-serif;font-size:7px;font-weight:600;letter-spacing:.2px}
  .hero--light .nav{color:var(--ink)}
  .nav__login{display:flex;align-items:center;gap:4px}

  .hero__rule{position:absolute;left:41px;top:77px;width:50px;height:2px;background:var(--white)}
  .hero__title{position:absolute;left:41px;width:290px;font-weight:700;font-size:16px;line-height:21px;text-shadow:0 1px 3px rgba(0,0,0,.35)}
  .concept--mountain .hero__title{top:86px;font-size:16.5px;line-height:22px}
  .concept--growth .hero__title{top:66px}
  .concept--meeting .hero__title{top:110px;left:44px}
  .hero__scroll{position:absolute;left:213px;top:183px}
  .concept--meeting .hero__scroll{left:43px;top:183px}

  .about{position:relative;height:194px}
  .mission{position:absolute;left:41px;top:24px;width:168px}
  .mission__label{font-family:"Montserrat",sans-serif;font-size:8px;color:var(--blue);font-weight:600;margin-bottom:8px}
  .mission__text{font-family:"Montserrat",sans-serif;font-size:11.6px;line-height:18px;white-space:nowrap}
  .mission__text b{font-weight:600}

  .offer{position:absolute;left:208px;width:192px;display:flex;gap:10px}
  .offer--ground{top:28px}
  .offer--special{top:120px}
  .offer__icon{width:42px;height:42px;flex:none}
  .offer__title{font-weight:700;font-size:9.5px;margin-bottom:6px}
  .offer__text{font-size:6.4px;line-height:10px;color:var(--muted)}

  .site-footer{position:absolute;left:0;right:0;bottom:0;height:106px;background:var(--footer);color:var(--white)}
  .site-footer .brand{top:12px;font-size:11px}
  .site-footer__contact{position:absolute;left:41px;top:50px;font-size:6.8px;line-height:11px}
  .site-footer__email{display:flex;align-items:center;gap:4px;font-weight:700}
  .site-footer__rule{position:absolute;left:41px;right:41px;top:81px;height:1px;background:var(--rule)}
  .site-footer__copy{position:absolute;left:41px;top:90px;font-size:5.6px}
</style>
</head>
<body>

<section class="concept concept--mountain">
  <header class="hero hero--light">
    <div class="hero__media" role="img" aria-label="Photo of a person with raised arms on a misty mountain peak"></div>
    <div class="brand"><span class="brand__mark"></span><span>HALVERN<br>BUILDERS</span></div>
    <nav class="nav">
      <svg width="15" height="9" viewBox="0 0 15 9" stroke="currentColor" stroke-width="1"><path d="M4 .5h11M2 3.5h13M5 6h10M0 8.5h15"/></svg>
      <span class="nav__login"><svg width="6" height="7" viewBox="0 0 6 7" fill="#0b5aa6"><circle cx="3" cy="1.7" r="1.6"/><path d="M0 7a3 3 0 0 1 6 0z"/></svg>INVESTOR LOGIN</span>
    </nav>
    <span class="hero__rule"></span>
    <h1 class="hero__title">Halvern Builders is an entrepreneurial firm focused on building and growing transformational companies</h1>
    <svg class="hero__scroll" width="14" height="28" viewBox="0 0 14 28" fill="none" stroke="#fff" stroke-width="1"><rect x=".5" y=".5" width="13" height="19" rx="6.5"/><path d="M7 4v3M7 20v7M5 25l2 2 2-2"/></svg>
  </header>
  <main class="about">
    <div class="mission">
      <p class="mission__label">MISSION</p>
      <p class="mission__text">Our mission is to build<br><b>meaningful</b> businesses that<br>create <b>enduring</b> value by<br>impacting people in a<br><b>measurable</b> way.</p>
    </div>
    <div class="offer offer--ground">
      <svg class="offer__icon" viewBox="0 0 42 42" fill="none" stroke-width="1.4"><rect x="6" y="6" width="30" height="30" rx="3" stroke="#555"/><path d="M21 30V13M14 20l7-7 7 7" stroke="#0b5aa6"/></svg>
      <div>
        <h2 class="offer__title">Ground Up</h2>
        <p class="offer__text">Our ground up business applies a proven analytic process to identify value edge, a form of competitive advantage. We architect transformational companies and are deliberate in creating the foundation necessary to lead an industry.</p>
      </div>
    </div>
    <div class="offer offer--special">
      <svg class="offer__icon" viewBox="0 0 42 42" fill="none" stroke-width="1.4"><circle cx="21" cy="21" r="15" stroke="#555"/><circle cx="21" cy="21" r="8" stroke="#555"/><circle cx="21" cy="21" r="2.5" fill="#0b5aa6" stroke="#0b5aa6"/></svg>
      <div>
        <h2 class="offer__title">Special Opportunities</h2>
        <p class="offer__text">We partner with exceptional teams that create value by transforming lives. Our investment focus includes large companies and spin-outs.</p>
      </div>
    </div>
  </main>
  <footer class="site-footer">
    <div class="brand"><span class="brand__mark"></span><span>HALVERN<br>BUILDERS</span></div>
    <div class="site-footer__contact">
      <p>For media inquiries, please contact</p>
      <p class="site-footer__email"><svg width="7" height="5" viewBox="0 0 7 5" fill="#fff"><path d="M0 0h7v5H0z"/><path d="M0 0l3.5 2.6L7 0" stroke="#231f20" stroke-width=".7" fill="none"/></svg>mara@halvernbuilders.com</p>
    </div>
    <span class="site-footer__rule"></span>
    <p class="site-footer__copy">Copyright © 2021, Halvern Builders.</p>
  </footer>
</section>

<section class="concept concept--growth">
  <header class="hero">
    <div class="hero__media" role="img" aria-label="Greyscale image of rising percentage arrows with one blue arrow and a businessman's hand"></div>
    <div class="brand"><span class="brand__mark"></span><span>HALVERN<br>BUILDERS</span></div>
    <nav class="nav">
      <svg width="15" height="9" viewBox="0 0 15 9" stroke="currentColor" stroke-width="1"><path d="M4 .5h11M2 3.5h13M5 6h10M0 8.5h15"/></svg>
      <span class="nav__login"><svg width="6" height="7" viewBox="0 0 6 7" fill="#fff"><circle cx="3" cy="1.7" r="1.6"/><path d="M0 7a3 3 0 0 1 6 0z"/></svg>INVESTOR LOGIN</span>
    </nav>
    <h1 class="hero__title">Halvern Builders is an entrepreneurial firm focused on building and growing transformational companies</h1>
    <svg class="hero__scroll" width="14" height="28" viewBox="0 0 14 28" fill="none" stroke="#fff" stroke-width="1"><rect x=".5" y=".5" width="13" height="19" rx="6.5"/><path d="M7 4v3M7 20v7M5 25l2 2 2-2"/></svg>
  </header>
  <main class="about">
    <div class="mission">
      <p class="mission__label">MISSION</p>
      <p class="mission__text">Our mission is to build<br><b>meaningful</b> businesses that<br>create <b>enduring</b> value by<br>impacting people in a<br><b>measurable</b> way.</p>
    </div>
    <div class="offer offer--ground">
      <svg class="offer__icon" viewBox="0 0 42 42" fill="none" stroke-width="1.4"><circle cx="21" cy="21" r="15" stroke="#555"/><path d="M21 29V13M15 19l6-6 6 6" stroke="#0b5aa6"/></svg>
      <div>
        <h2 class="offer__title">Ground Up</h2>
        <p class="offer__text">Our ground up business applies a proven analytic process to identify value edge, a form of competitive advantage. We architect transformational companies and are deliberate in creating the foundation necessary to lead an industry.</p>
      </div>
    </div>
    <div class="offer offer--special">
      <svg class="offer__icon" viewBox="0 0 42 42" fill="none" stroke-width="1.4"><circle cx="21" cy="21" r="15" stroke="#555"/><path d="M21 13v16M13 21h16" stroke="#0b5aa6"/></svg>
      <div>
        <h2 class="offer__title">Special Opportunities</h2>
        <p class="offer__text">We partner with exceptional teams that create value by transforming lives. Our investment focus includes large companies and spin-outs.</p>
      </div>
    </div>
  </main>
  <footer class="site-footer">
    <div class="brand"><span class="brand__mark"></span><span>HALVERN<br>BUILDERS</span></div>
    <div class="site-footer__contact">
      <p>For media inquiries, please contact</p>
      <p class="site-footer__email"><svg width="7" height="5" viewBox="0 0 7 5" fill="#fff"><path d="M0 0h7v5H0z"/><path d="M0 0l3.5 2.6L7 0" stroke="#231f20" stroke-width=".7" fill="none"/></svg>mara@halvernbuilders.com</p>
    </div>
    <span class="site-footer__rule"></span>
    <p class="site-footer__copy">Copyright © 2021, Halvern Builders.</p>
  </footer>
</section>

<section class="concept concept--meeting">
  <header class="hero">
    <div class="hero__media" role="img" aria-label="Greyscale photo of business partners shaking hands across a meeting table"></div>
    <div class="brand"><span class="brand__mark"></span><span>HALVERN<br>BUILDERS</span></div>
    <nav class="nav">
      <svg width="15" height="9" viewBox="0 0 15 9" stroke="currentColor" stroke-width="1"><path d="M4 .5h11M2 3.5h13M5 6h10M0 8.5h15"/></svg>
      <span class="nav__login"><svg width="6" height="7" viewBox="0 0 6 7" fill="#fff"><circle cx="3" cy="1.7" r="1.6"/><path d="M0 7a3 3 0 0 1 6 0z"/></svg>INVESTOR LOGIN</span>
    </nav>
    <h1 class="hero__title">Halvern Builders is an entrepreneurial firm focused on building and growing transformational companies</h1>
    <svg class="hero__scroll" width="14" height="28" viewBox="0 0 14 28" fill="none" stroke="#fff" stroke-width="1"><rect x=".5" y=".5" width="13" height="19" rx="6.5"/><path d="M7 4v3M7 20v7M5 25l2 2 2-2"/></svg>
  </header>
  <main class="about">
    <div class="mission">
      <p class="mission__label">MISSION</p>
      <p class="mission__text">Our mission is to build<br><b>meaningful</b> businesses that<br>create <b>enduring</b> value by<br>impacting people in a<br><b>measurable</b> way.</p>
    </div>
    <div class="offer offer--ground">
      <svg class="offer__icon" viewBox="0 0 42 42" fill="none" stroke-width="1.4"><circle cx="21" cy="21" r="15" stroke="#555"/><path d="M21 29V13M15 19l6-6 6 6" stroke="#0b5aa6"/></svg>
      <div>
        <h2 class="offer__title">Ground Up</h2>
        <p class="offer__text">Our ground up business applies a proven analytic process to identify value edge, a form of competitive advantage. We architect transformational companies and are deliberate in creating the foundation necessary to lead an industry.</p>
      </div>
    </div>
    <div class="offer offer--special">
      <svg class="offer__icon" viewBox="0 0 42 42" fill="none" stroke-width="1.4"><circle cx="21" cy="21" r="15" stroke="#555"/><path d="M21 13v16M13 21h16" stroke="#0b5aa6"/></svg>
      <div>
        <h2 class="offer__title">Special Opportunities</h2>
        <p class="offer__text">We partner with exceptional teams that create value by transforming lives. Our investment focus includes large companies and spin-outs.</p>
      </div>
    </div>
  </main>
  <footer class="site-footer">
    <div class="brand"><span class="brand__mark"></span><span>HALVERN<br>BUILDERS</span></div>
    <div class="site-footer__contact">
      <p>For media inquiries, please contact</p>
      <p class="site-footer__email"><svg width="7" height="5" viewBox="0 0 7 5" fill="#fff"><path d="M0 0h7v5H0z"/><path d="M0 0l3.5 2.6L7 0" stroke="#231f20" stroke-width=".7" fill="none"/></svg>mara@halvernbuilders.com</p>
    </div>
    <span class="site-footer__rule"></span>
    <p class="site-footer__copy">Copyright © 2021, Halvern Builders.</p>
  </footer>
</section>

</body>
</html>
```